BUSINESS CARD - HALVERDINE RURAL SERVICES

I would like to create a business card for my fertilizer spreading business. I would like to incorporate my existing logo and also a description of the services offered. The business card will be given to farmers so must be kept simple but effective. It will also be left in stores so much also be eye catching in order to stand out from other cards.

Target Market(s)

FARMERS

Requirements
Must have
• FRONT OF CARD = EXISTING LOGO + "CUSTOMISED SPREADING" below the logo

REAR Of CARD = SERVICES OFFERED AND CONTACT DETAILS

- Bulk fertilizer including Lime, Gypsum, Manure & Compost
- Granular fertilizer including Single Super, Urea, Gran-am, & Custom Blends
- Modern equipment - Autosteer & Variable Rate Capable
- Friendly & Reliable Service
- Contact Gus: 0471 502 318
Nice to have
• utilize same color scheme as existing logo

```html
<!DOCTYPE html>
<html lang="en">
<head>
<meta charset="utf-8">
<title>Halverdine Rural Services – Business Cards</title>
<link href="https://fonts.googleapis.com/css2?family=Montserrat:wght@400;500;600;700&family=Roboto:wght@400&display=swap" rel="stylesheet">
<style>
  :root {
    --stage: #000000;
    --card: #ffffff;
    --charcoal: #58585a;
    --orange: #f7941d;
    --text-grey: #4a4a4a;
  }
  html, body {
    margin: 0;
    padding: 0;
    width: 1200px;
    height: 1200px;
    overflow: hidden;
    background: var(--stage);
  }
  .sheet {
    position: relative;
    width: 1200px;
    height: 1200px;
  }
  .card {
    position: absolute;
    width: 453px;
    height: 259px;
    background: var(--card);
    overflow: hidden;
    font-family: "Montserrat", sans-serif;
  }
  .card--front-a { left: 106px; top: 289px; }
  .card--back-a  { left: 600px; top: 289px; }
  .card--front-b { left: 106px; top: 619px; }
  .card--back-b  { left: 600px; top: 619px; }

  .mark {
    position: absolute;
    border-radius: 50%;
    background: var(--charcoal);
  }
  .front .mark { width: 90px; height: 90px; left: 181px; top: 58px; }
  .back  .mark { width: 66px; height: 66px; left: 193px; top: 30px; }

  .brand-name {
    position: absolute;
    left: 0; right: 0;
    text-align: center;
    font-weight: 700;
    color: var(--charcoal);
    letter-spacing: -0.3px;
    white-space: nowrap;
  }
  .front .brand-name { top: 150px; font-size: 19px; }
  .back  .brand-name { top: 100px; font-size: 15px; }

  .tagline {
    position: absolute;
    left: 0; right: 0;
    top: 186px;
    text-align: center;
    font-size: 14px;
    font-weight: 500;
    color: var(--charcoal);
    letter-spacing: 0.6px;
  }

  .highlights {
    position: absolute;
    left: 0; right: 0;
    top: 145px;
    margin: 0;
    padding: 0;
    list-style: none;
    text-align: center;
    color: var(--orange);
    font-size: 10.5px;
    font-weight: 500;
    line-height: 16px;
    letter-spacing: 0.2px;
  }

  .services {
    position: absolute;
    left: 0; right: 0;
    top: 190px;
    margin: 0;
    padding: 0;
    list-style: none;
    text-align: center;
    font-family: "Roboto", sans-serif;
    color: var(--text-grey);
    font-size: 10px;
    line-height: 16px;
  }
  .services .sep { margin: 0 5px; }

  .contact-band {
    position: absolute;
    left: 0; right: 0; bottom: 0;
    height: 21px;
    line-height: 21px;
    text-align: center;
    color: #ffffff;
    font-size: 10.5px;
    font-weight: 500;
    letter-spacing: 0.3px;
  }
  .contact-band--orange { background: var(--orange); }
  .contact-band--charcoal { background: var(--charcoal); }
</style>
</head>
<body>
<main class="sheet">

  <section class="card front card--front-a">
    <div class="mark"></div>
    <div class="brand-name">HALVERDINE RURAL SERVICES</div>
    <div class="tagline">CUSTOMISED SPREADING</div>
  </section>

  <section class="card back card--back-a">
    <div class="mark"></div>
    <div class="brand-name">HALVERDINE RURAL SERVICES</div>
    <ul class="highlights">
      <li>Modern Equipment Autosteer &amp; Variable Rate Capable</li>
      <li>Friendly &amp; Reliable Services</li>
    </ul>
    <ul class="services">
      <li>Bulk fertilizer including Lime<span class="sep">•</span>Gypsum<span class="sep">•</span>Manure &amp; Composts</li>
      <li>Granular fertilizer including Single Super<span class="sep">•</span>Urea<span class="sep">•</span>Gran-am &amp; Custom Blends</li>
    </ul>
    <div class="contact-band contact-band--orange">Contact Gus : 0471 502 318</div>
  </section>

  <section class="card front card--front-b">
    <div class="mark"></div>
    <div class="brand-name">HALVERDINE RURAL SERVICES</div>
    <div class="tagline">CUSTOMISED SPREADING</div>
  </section>

  <section class="card back card--back-b">
    <div class="mark"></div>
    <div class="brand-name">HALVERDINE RURAL SERVICES</div>
    <ul class="highlights">
      <li>Modern Equipment Autosteer &amp; Variable Rate Capable</li>
      <li>Friendly &amp; Reliable Services</li>
    </ul>
    <ul class="services">
      <li>Bulk fertilizer including Lime<span class="sep">•</span>Gypsum<span class="sep">•</span>Manure &amp; Composts</li>
      <li>Granular fertilizer including Single Super<span class="sep">•</span>Urea<span class="sep">•</span>Gran-am &amp; Custom Blends</li>
    </ul>
    <div class="contact-band contact-band--charcoal">Contact Gus : 0471 502 318</div>
  </section>

</main>
</body>
</html>
```